Make the design for the landing page of BrightKettle.com

Quillstack is framework (software to build websites)
Goal:
Build a professional landing page to offer free Quillstack consultancy sessions in exchange for an email address and to promote your paid services.
🎯 Primary Objective
Convert visitors into leads by offering a free Quillstack code audit or strategy session. Capture their email and optionally allow them to directly book a call or hire your services.
🧠 Target Audience
>Companies and startups with Quillstack apps
>CTOs and tech leads managing legacy Quillstack code
>Freelance developers looking to improve their architecture
>Product owners facing bugs or scaling issues
📐 Suggested Page Structure
1. Hero Section (Top of Page - Above the Fold)
Headline (focused on pain/problem):
“Is your Quillstack app slow, outdated or full of bugs?”
Subheadline (clear promise of value):
“Book a free Quillstack code audit and get actionable insights in just 30 minutes.”
Primary CTA (email capture form):
Email input
Button: “Schedule Free Consultation”
Secondary CTA Button:
“Free Consultancy” or “Hire My Services”
✅ Make this CTA bold, highly visible, and frictionless
✅ You can use Calendly, TidyCal, or a simple form for scheduling
2. Section: “Are you struggling with any of these?”
Use a vertical scroll experience with checkmarks or icons to highlight common pain points:
🔼 Upgrading Runtime / Quillstack
🧪 No automated tests
🐛 Recurring bugs
🔐 Security issues
🐢 Slow performance
🧱 Messy architecture or no clear structure
📦 Outdated packages / dependencies
Make this visually engaging — for example, animated list items as the user scrolls down.
3. What You Get With a Free Audit
A personalized code review or system analysis
Architecture & performance insights
No commitment, no spam
+12 years of Quillstack experience
Delivered via a video call or written feedback
4. About Me / Why Trust Me
Short section introducing you:
Your experience with Quillstack (12+ years)
Notable companies, projects, or logos (if any)
CodeVault / Inkpost / Open Source contributions
Maybe include a friendly photo or avatar
5. Call to Action (Repeat CTA)
Reinforce the offer:
“Let’s fix your Quillstack headaches together — for free.”
Button: “Book My Free Call”
Optional email input form again (for easy access)
6. Testimonials (Optional but Recommended)
If you already have satisfied clients:
2-3 short quotes with names and roles
Example: “Tobías helped us restructure our legacy Quillstack codebase in a week. Highly recommended!”
7. FAQ Section (Optional)
Common questions to eliminate hesitation:
What happens after I submit my email?
Is the consultancy really free?
What kind of projects do you work with?
How long does the call last?
8. Footer
Quick access buttons:
“Schedule Consultation”
“Hire My Services”
Contact email
Linked social profiles or GitHub
✨ Design Style & Inspirations
Clean, minimalist layout (like plumfernworks.io, but with more obvious CTAs)
Technical yet friendly tone
Use soft animations and icons to break sections
What I would like to see?
An obvious CTA in the middle to the page in order to schedule a 30-mins free consultancy .
also a when you scroll you will see something like
"These problems are common for you"
With the list of common Runtime/Quillstack problems.
Also would like a button in the top right that says
"Audit me now" like "Get unstuck" in https://plumfernworks.io/
Take inspiration from:
https://plumfernworks.io/
https://www.zelvanhub.io/
Use this as the logo
https://quorbixfield48.pagelet.site/png/logo
Consultancy Project
1 page

```html
<!DOCTYPE html>
<html lang="en">
<head>
<meta charset="utf-8">
<title>BrightKettle – Free Quillstack Code Audit</title>
<link href="https://fonts.googleapis.com/css2?family=Figtree:wght@500;600;700;800&family=Arimo:wght@400;500;700&display=swap" rel="stylesheet">
<style>
:root{
  --red:#ee1d23;
  --red-deep:#d91920;
  --pink:#fde3e5;
  --pink-soft:#fff1f2;
  --ink:#222326;
  --text:#333;
  --muted:#666;
  --footer:#f4f4f4;
  --white:#fff;
}
*{margin:0;padding:0;box-sizing:border-box}
html,body{width:1200px;height:3627px;overflow:hidden}
body{position:relative;background:var(--white);font-family:"Arimo",Arial,sans-serif;color:var(--text)}
.abs{position:absolute}
.h{font-family:"Figtree",Arial,sans-serif;color:var(--ink);font-weight:700}
.pill{border-radius:40px;display:flex;align-items:center;justify-content:center;font-weight:700;font-size:14px;white-space:nowrap}
.pill-soft{background:var(--pink);color:var(--red)}
.pill-red{background:var(--red);color:var(--white)}

/* header */
.hero-glow{left:0;top:0;width:1200px;height:680px;background:
 radial-gradient(circle at 60px 190px,rgba(249,170,175,.45),transparent 150px),
 radial-gradient(ellipse at 1000px 120px,rgba(252,205,208,.5),transparent 320px),
 linear-gradient(#fff,#fff)}
.logo{left:145px;top:16px;width:168px;height:38px;font-size:19px;font-family:"Figtree",sans-serif}
.nav{left:481px;top:25px;display:flex;gap:30px;font-size:14px;color:var(--ink)}
.nav .active{color:var(--red)}
.nav-cta{left:903px;top:16px;width:152px;height:38px;font-size:15px}

.hero-title{left:0;width:1200px;top:150px;text-align:center;font-size:42px;line-height:49px}
.hero-sub{left:0;width:1200px;top:255px;text-align:center;font-size:14px;font-weight:700;color:var(--ink)}
.hero-form{left:335px;top:293px;width:528px;height:44px;background:#fff;border-radius:30px;box-shadow:0 3px 14px rgba(0,0,0,.12);display:flex;align-items:center;padding:0 4px 0 28px}
.hero-form span{flex:1;font-size:14px;color:#444}
.hero-form .pill{width:232px;height:36px;font-size:14px}
.hero-cta2{left:515px;top:359px;width:169px;height:36px;font-size:14px}
.wave{left:0;top:395px;width:1200px;height:270px;background:
 radial-gradient(ellipse 700px 90px at 600px 140px,rgba(240,80,88,.28),transparent 70%),
 radial-gradient(ellipse 500px 70px at 300px 120px,rgba(240,80,88,.18),transparent 70%),
 radial-gradient(ellipse 500px 80px at 950px 80px,rgba(240,80,88,.2),transparent 70%)}

/* pain points */
.sec-title{left:0;width:1200px;text-align:center;font-size:32px}
.pain{left:198px;display:flex;align-items:center;gap:28px;font-size:16px;font-weight:700;color:var(--ink)}
.pain .ico{width:74px;height:74px;border-radius:50%;background:var(--pink);display:flex;align-items:center;justify-content:center}
.photo{background:linear-gradient(135deg,#c9d3dc,#8f99a3 55%,#c6672a)}
.divider{left:155px;width:894px;height:2px;background:linear-gradient(90deg,transparent,var(--red),transparent)}

/* audit list */
.get-title{left:632px;top:1258px;font-size:32px;line-height:40px}
.get-list{left:632px;top:1353px;list-style:none}
.get-list li{display:flex;align-items:center;gap:17px;height:40px;font-size:15px;color:var(--ink)}
.tick{width:15px;height:15px;border-radius:50%;background:var(--red);display:flex;align-items:center;justify-content:center}

/* about */
.about-item{width:300px;text-align:center;font-size:15px;line-height:24px;color:var(--ink)}
.about-item .sq{width:97px;height:97px;margin:0 auto 14px;background:var(--red);border-radius:8px;display:flex;align-items:center;justify-content:center}
.vline{width:1px;height:150px;background:#bbb;top:1788px}

/* cta band */
.band{left:0;top:2056px;width:1200px;height:298px;background:var(--pink-soft)}
.band-title{left:142px;top:2116px;font-size:33px;line-height:40px}

/* testimonials */
.card{width:362px;height:217px;background:#fff;border-radius:10px;box-shadow:0 4px 22px rgba(0,0,0,.09);padding:30px 24px 0 70px}
.stars{color:#f39a0b;font-size:15px;letter-spacing:2px}
.card p{margin-top:12px;font-size:15px;line-height:24px;text-align:justify;color:#333}
.card .who{margin-top:10px;font-family:"Figtree",sans-serif;font-weight:700;font-size:18px;color:var(--ink)}
.card .who small{font-family:"Arimo",sans-serif;font-weight:400;font-size:12px;color:#555;margin-left:8px}
.avatar{width:124px;height:124px;border-radius:50%;background:linear-gradient(160deg,#d9dde2,#8a6a52)}

/* faq */
.faq-band{left:0;top:2858px;width:1200px;height:424px;background:linear-gradient(120deg,#e8141b,var(--red) 50%,#f0232a)}
.faq-title{left:144px;top:2915px;color:#fff;font-size:49px;line-height:56px;font-weight:800}
.faq{left:515px;width:540px;height:58px;background:#fff;border-radius:30px;box-shadow:0 0 0 3px rgba(255,255,255,.5);display:flex;align-items:center;justify-content:space-between;padding:0 8px 0 26px;font-size:15px;color:var(--ink)}
.faq b{width:40px;height:40px;border-radius:50%;background:var(--red);color:#fff;display:flex;align-items:center;justify-content:center;font-weight:400;font-size:18px}

/* footer */
.footer{left:0;top:3282px;width:1200px;height:345px;background:var(--footer)}
.f-btn{left:151px;width:201px;height:36px;font-size:14px}
.social{width:30px;height:30px;border-radius:50%;border:1.5px solid var(--ink);top:3463px}
.social.on{background:var(--red);border-color:var(--red)}
.f-col{top:3349px}
.f-col h4{font-family:"Figtree",sans-serif;font-size:21px;color:var(--ink);font-weight:700}
.f-col h4::after{content:"";display:block;width:40px;height:2px;background:var(--red);margin-top:8px}
.f-col ul{list-style:none;margin-top:12px}
.f-col li{font-size:14px;line-height:24px;color:#333}
.contact li{display:flex;gap:22px;margin-bottom:14px;line-height:19px}
.copy{left:0;width:1200px;top:3574px;text-align:center;font-size:13px;color:#333}
</style>
</head>
<body>

<!-- Hero -->
<div class="abs hero-glow"></div>
<div class="abs logo pill pill-soft">BrightKettle</div>
<nav class="abs nav"><span class="active">Home</span><span>About</span><span>Service</span><span>Blog</span><span>Contact</span></nav>
<div class="abs nav-cta pill pill-soft">Audit me Now</div>

<h1 class="abs hero-title h">Is your Quillstack app slow,<br>outdated or full of bugs?</h1>
<p class="abs hero-sub">Book a free Quillstack code audit and get actionable insights in just 30 minutes.</p>
<div class="abs hero-form"><span>Enter your email</span><div class="pill pill-soft">Schedule Free Consultation</div></div>
<div class="abs hero-cta2 pill pill-red">Free Consultancy</div>
<div class="abs wave" role="img" aria-label="Flowing wave of soft red dots across the page"></div>

<!-- Pain points -->
<h2 class="abs sec-title h" style="top:658px">Are you struggling with any of these?</h2>
<div class="abs pain" style="top:730px"><span class="ico"><svg width="34" height="34" viewBox="0 0 34 34" fill="none" stroke="#ee1d23" stroke-width="1.6"><path d="M8 3h13l6 6v22H8z"/><path d="M14 14l-3 3 3 3M20 14l3 3-3 3"/><rect x="5" y="23" width="16" height="7"/></svg></span>Upgrading Runtime / Quillstack</div>
<div class="abs pain" style="top:811px"><span class="ico"><svg width="34" height="34" viewBox="0 0 34 34" fill="none" stroke="#ee1d23" stroke-width="1.6"><rect x="5" y="4" width="18" height="25"/><path d="M9 10h8M9 15h6M9 20h5"/><circle cx="22" cy="21" r="5"/><path d="M26 25l4 4"/></svg></span>No automated tests</div>
<div class="abs pain" style="top:889px"><span class="ico"><svg width="34" height="34" viewBox="0 0 34 34" fill="none" stroke="#ee1d23" stroke-width="1.6"><rect x="5" y="6" width="24" height="18"/><path d="M11 29h12M17 24v5"/><circle cx="17" cy="15" r="5"/><path d="M13 11l-3-3M21 11l3-3"/></svg></span>Recurring bugs</div>
<div class="abs pain" style="top:968px"><span class="ico"><svg width="34" height="34" viewBox="0 0 34 34" fill="none" stroke="#ee1d23" stroke-width="1.6"><rect x="4" y="5" width="26" height="19"/><path d="M12 29h10"/><path d="M17 9l5 2v4c0 3-2 5-5 6-3-1-5-3-5-6v-4z"/></svg></span>Security issues</div>
<div class="abs pain" style="top:1049px"><span class="ico"><svg width="34" height="34" viewBox="0 0 34 34" fill="none" stroke="#ee1d23" stroke-width="1.6"><circle cx="17" cy="17" r="12"/><circle cx="17" cy="17" r="7"/><path d="M17 17l4-4"/></svg></span>Slow performance</div>
<div class="abs photo" style="left:589px;top:746px;width:414px;height:359px;border-radius:55% 45% 48% 52%/50% 52% 48% 50%" role="img" aria-label="Developer with glasses in an orange shirt writing on a whiteboard in an office"></div>

<div class="abs divider" style="top:1190px"></div>

<!-- What you get -->
<div class="abs photo" style="left:166px;top:1246px;width:408px;height:356px;border-radius:48% 52% 50% 50%/55% 50% 50% 45%;background:linear-gradient(135deg,#55614f,#b9ab95 50%,#e0d7c8)" role="img" aria-label="Smiling professional in a light blazer seated at a desk"></div>
<h2 class="abs get-title h">What You Get With<br>a Free Audit</h2>
<ul class="abs get-list">
  <li><span class="tick"><svg width="9" height="9" viewBox="0 0 9 9"><path d="M1.5 4.5l2 2 4-4" stroke="#fff" stroke-width="1.6" fill="none"/></svg></span>A personalized code review or system analysis</li>
  <li><span class="tick"><svg width="9" height="9" viewBox="0 0 9 9"><path d="M1.5 4.5l2 2 4-4" stroke="#fff" stroke-width="1.6" fill="none"/></svg></span>Architecture &amp; performance insights</li>
  <li><span class="tick"><svg width="9" height="9" viewBox="0 0 9 9"><path d="M1.5 4.5l2 2 4-4" stroke="#fff" stroke-width="1.6" fill="none"/></svg></span>No commitment, no spam</li>
  <li><span class="tick"><svg width="9" height="9" viewBox="0 0 9 9"><path d="M1.5 4.5l2 2 4-4" stroke="#fff" stroke-width="1.6" fill="none"/></svg></span>+12 years of Quillstack experience</li>
  <li><span class="tick"><svg width="9" height="9" viewBox="0 0 9 9"><path d="M1.5 4.5l2 2 4-4" stroke="#fff" stroke-width="1.6" fill="none"/></svg></span>Delivered via a video call or written feedback</li>
</ul>
<div class="abs pill pill-soft" style="left:632px;top:1556px;width:307px;height:37px">Schedule a 30-mins Free Consultancy</div>

<div class="abs divider" style="top:1652px"></div>

<!-- About -->
<h2 class="abs sec-title h" style="top:1710px">About Me</h2>
<div class="abs about-item" style="left:146px;top:1788px"><div class="sq"><svg width="50" height="54" viewBox="0 0 50 54" fill="#fff"><rect x="6" y="2" width="30" height="44" rx="4"/><rect x="12" y="11" width="18" height="4" fill="#ee1d23"/><rect x="12" y="19" width="18" height="4" fill="#ee1d23"/><rect x="12" y="27" width="12" height="4" fill="#ee1d23"/><circle cx="38" cy="40" r="9" stroke="#ee1d23" stroke-width="3"/></svg></div>Your experience with<br>Quillstack (12+ years)</div>
<div class="abs vline" style="left:448px"></div>
<div class="abs about-item" style="left:448px;top:1788px"><div class="sq"><svg width="52" height="54" viewBox="0 0 52 54" fill="#fff"><rect x="10" y="4" width="32" height="46"/><rect x="2" y="48" width="48" height="4"/><g fill="#ee1d23"><rect x="16" y="12" width="5" height="5"/><rect x="24" y="12" width="5" height="5"/><rect x="32" y="12" width="5" height="5"/><rect x="16" y="21" width="5" height="5"/><rect x="24" y="21" width="5" height="5"/><rect x="32" y="21" width="5" height="5"/><rect x="16" y="30" width="5" height="5"/><rect x="24" y="30" width="5" height="5"/><rect x="32" y="30" width="5" height="5"/><rect x="22" y="39" width="9" height="11"/></g></svg></div>Notable companies</div>
<div class="abs vline" style="left:749px"></div>
<div class="abs about-item" style="left:752px;top:1788px"><div class="sq"><svg width="52" height="44" viewBox="0 0 52 44" fill="none" stroke="#fff" stroke-width="5" stroke-linecap="round"><path d="M16 8L4 22l12 14M36 8l12 14-12 14M30 4L22 40"/></svg></div>CodeVault / Inkpost /<br>Open Source contributions</div>

<!-- CTA band -->
<div class="abs band"></div>
<h2 class="abs band-title h">Let’s fix your Quillstack<br>headaches together<br>— for free.</h2>
<div class="abs pill pill-soft" style="left:144px;top:2250px;width:202px;height:35px">Book My Free Call</div>
<svg class="abs" style="left:540px;top:1995px" width="520" height="420" viewBox="0 0 520 420" role="img" aria-label="Two tilted capsule photos: a smiling professional and hands joining puzzle pieces">
  <defs>
    <linearGradient id="capA" x1="0" y1="0" x2="0" y2="1"><stop offset="0" stop-color="#a9b4a6"/><stop offset=".6" stop-color="#8f8a5f"/><stop offset="1" stop-color="#e9ece6"/></linearGradient>
    <linearGradient id="capB" x1="0" y1="0" x2="0" y2="1"><stop offset="0" stop-color="#9fb2a7"/><stop offset=".5" stop-color="#4c5e52"/><stop offset="1" stop-color="#2e3b33"/></linearGradient>
  </defs>
  <rect x="55" y="12" width="205" height="392" rx="102" fill="url(#capA)" transform="rotate(18 157 208)"/>
  <rect x="270" y="12" width="205" height="392" rx="102" fill="url(#capB)" transform="rotate(18 372 208)"/>
</svg>

<!-- Testimonials -->
<h2 class="abs sec-title h" style="top:2472px">Testimonials</h2>
<svg class="abs" style="left:82px;top:2640px" width="20" height="30" viewBox="0 0 20 30"><path d="M15 3L4 15l11 12" stroke="#222" stroke-width="3" fill="none"/></svg>
<svg class="abs" style="left:1098px;top:2640px" width="20" height="30" viewBox="0 0 20 30"><path d="M5 3l11 12L5 27" stroke="#222" stroke-width="3" fill="none"/></svg>
<div class="abs card" style="left:218px;top:2543px">
  <div class="stars">★★★★★</div>
  <p>Lorem ipsum dolor sit amet, consectetur adipiscing elit, sed do eiusmod tempor incididunt ut labore et dolore magna aliqua.</p>
  <div class="who">John doe<small>Company name</small></div>
</div>
<div class="abs avatar" style="left:146px;top:2589px" role="img" aria-label="Client portrait"></div>
<div class="abs card" style="left:697px;top:2543px">
  <div class="stars">★★★★★</div>
  <p>Lorem ipsum dolor sit amet, consectetur adipiscing elit, sed do eiusmod tempor incididunt ut labore et dolore magna aliqua.</p>
  <div class="who">John doe<small>Company name</small></div>
</div>
<div class="abs avatar" style="left:625px;top:2589px;background:linear-gradient(160deg,#9fd0ef,#2f6fa8)" role="img" aria-label="Client portrait"></div>

<!-- FAQ -->
<div class="abs faq-band"></div>
<h2 class="abs faq-title h" style="color:#fff">Frequently<br>Asked<br>Questions</h2>
<div class="abs faq" style="top:2929px">What happens after I submit my email?<b>+</b></div>
<div class="abs faq" style="top:3001px">Is the consultancy really free?<b>+</b></div>
<div class="abs faq" style="top:3073px">What kind of projects do you work with?<b>+</b></div>
<div class="abs faq" style="top:3145px">How long does the call last?<b>+</b></div>

<!-- Footer -->
<div class="abs footer"></div>
<div class="abs f-btn pill pill-soft" style="top:3358px">Schedule Consultation</div>
<div class="abs f-btn pill pill-soft" style="top:3406px">Hire My Services</div>
<span class="abs social" style="left:206px" aria-label="Social profile"></span>
<span class="abs social on" style="left:243px" aria-label="Social profile"></span>
<span class="abs social" style="left:278px" aria-label="Social profile"></span>

<div class="abs f-col" style="left:444px"><h4>Quick Links</h4><ul><li>Home</li><li>About Us</li><li>Services</li><li>Blog</li><li>Contact</li></ul></div>
<div class="abs f-col" style="left:652px"><h4>Links</h4><ul><li>Privacy Policy</li><li>Terms of Service</li><li>Blog</li><li>Faq</li><li>Contact</li></ul></div>
<div class="abs f-col contact" style="left:860px"><h4>Contact Us</h4><ul>
  <li><svg width="10" height="14" viewBox="0 0 10 14"><path d="M5 0a5 5 0 015 5c0 4-5 9-5 9S0 9 0 5a5 5 0 015-5z" fill="#ee1d23"/><circle cx="5" cy="5" r="2" fill="#f4f4f4"/></svg><span>123, Lorem ipsum dolor<br>sit amet</span></li>
  <li><svg width="12" height="12" viewBox="0 0 12 12"><path d="M2 0l3 3-1.5 2a7 7 0 003.5 3.5L9 7l3 3-2 2C5 12 0 7 0 2z" fill="#ee1d23"/></svg><span>+1 888 888 8888</span></li>
  <li><svg width="13" height="10" viewBox="0 0 13 10"><rect width="13" height="10" fill="#ee1d23"/><path d="M0 0l6.5 5L13 0" stroke="#f4f4f4" fill="none"/></svg><span>info@companyname.com</span></li>
</ul></div>
<p class="abs copy">© Copyrights 2025 | All Rights Reserved</p>

</body>
</html>
```